Modern Small Law Firm Website To Look Cutting Edge

I need a website design for a new, single-attorney law firm. The firm will be called "The Hollowmere Law Group." Our goal is to handle car accident and general personal injury lawsuits for individuals.

Our selling points are: (1) We charge less so you keep more; (2) We have experience and success trying and settling multi-million dollar cases; (3) We use modern technology to make the whole process simple, easy and hassle-free for clients.

Also because we are a one-man law firm, the clients will personally know the lawyer and have access to them. For that reason, I thought a good big tagline for the website would be "KNOW YOUR LAWYER"

I like the idea of splitting the website vertically down the middle, with the left side having a blue background, a picture of me, and big white lettering for the tagline, and the right side having a white background with blue lettering and headlines. I don't want navy blue or royal blue, but a more bright and eye-catching blue color. We can experiment with different shades.

I would be curious about how it could look with some minor orange accent coloring somewhere.

I need to feature prominently, probably in the top left corner, this phone number: 504-617-2093.

This will be used as much by mobile users as it would be by desktop/computer users.

The final design should communicate trust, convenience and cutting edge technology that leads to success.

Finally, I would be curious how we can have a sleek looking info submission box somewhere on the right side nearer the bottom that features different combinations of presenting these phrases: "QUICK QUESTION? QUICK ANSWER" The info submission button could say "Ask"

I am uploading two different pictures of me that can be used. The gray backgrounds are not necessary or good, if there is a way to cut them out that would be great. I can try and get that if needed.

Target Market(s)

Individuals who have been hurt by others, mostly in car accidents. They will be frustrated, inconvenienced and need to be soothed.

Industry/Entity Type

Legal

Number of Pages Required

1 page

Font styles to use
Sans Serif

Colors
0692cd
33a6d7
85cae6
faa54b
f78f20
3276b5

Requirements
Must have
• If you have started designing already, please note that the project description information is more important than the image that I uploaded originally. It has since been deleted.
• Also please now use the color photo that has been uploaded.
Nice to have
• I really want a clean and simple website design with not a lot of clutter. I'd like to avoid the typical law firm websites that you see that have tool bars across the top and basic borders/columns everywhere. It needs to grab your attention and look a little more cutting edge and different.
• Let's experiment with different eye-catching ways to present the three value propositions I noted.
• Also if the screen is split vertically with the left and right side being blue and white, maybe we can experiment with different ways that the two colors could fade into each other as opposed to just a line where one color starts and the other ends.
• And maybe the blue/white backgrounds could be textured somehow so that they don't appear flat. Perhaps we could try using differing shades of blue to give the appearance of pattern or 3D texture.
Should not have
• The basic picture/design I uploaded is just a suggestion, but there isn't really anything there.

```html
<!DOCTYPE html>
<html lang="en">
<head>
<meta charset="utf-8">
<title>Hollowmere Law Group</title>
<link href="https://fonts.googleapis.com/css2?family=Lato:wght@400;700;900&display=swap" rel="stylesheet">
<style>
:root{
  --blue:#33a6d7;
  --blue-deep:#0692cd;
  --blue-soft:#85cae6;
  --orange:#f78f20;
  --orange-soft:#faa54b;
  --ink:#333;
  --muted:#555;
  --grey-bg:#eeeeee;
  --dark-bar:#4a4a4a;
  --white:#fff;
}
*{box-sizing:border-box;margin:0;padding:0}
html,body{width:1200px;height:2941px;overflow:hidden}
body{font-family:"Lato",Arial,sans-serif;color:var(--ink);background:var(--white);position:relative}
.abs{position:absolute}

/* header + hero */
.hero{position:absolute;left:0;top:0;width:1200px;height:588px;
  background:linear-gradient(180deg,#ffffff 0%,#eef7fb 10%,#bfe2f1 40%,#7cc4e4 75%,#5ab4dc 100%)}
.logo{position:absolute;left:58px;top:12px;font-size:30px;font-weight:700;color:#6b6b6b;letter-spacing:0;line-height:34px}
.nav{position:absolute;right:40px;top:20px;display:flex;gap:32px;font-size:15px;color:#333;text-transform:uppercase}
.nav .active{border-bottom:4px solid var(--blue);padding-bottom:4px}
.hero-frame{position:absolute;left:43px;top:163px;width:1114px;height:318px;border:1px solid rgba(255,255,255,.85)}
.hero-kicker{position:absolute;left:0;width:1200px;top:155px;text-align:center;font-size:11px;font-weight:700;color:#333;letter-spacing:.5px}
.hero-kicker span{background:#cfe9f5;padding:0 12px}
.hero-title{position:absolute;left:0;width:1200px;top:215px;text-align:center;font-size:43px;color:var(--white);font-weight:400;letter-spacing:.5px}
.hero-title b{font-weight:900}
.hero-copy{position:absolute;left:330px;width:540px;top:270px;text-align:center;font-size:19.5px;line-height:24px;color:var(--white)}
.hero-btn{position:absolute;left:541px;top:357px;width:163px;height:39px;background:var(--blue);color:var(--white);font-size:18px;text-align:center;line-height:39px;font-weight:700}
.portrait{position:absolute;top:127px;height:461px;border-radius:4px 4px 0 0}
.portrait.left{left:29px;width:383px;background:linear-gradient(180deg,#c7a590 0%,#3a3a3a 40%,#1c1c1c 100%)}
.portrait.right{left:824px;width:362px;background:linear-gradient(180deg,#d8b29a 0%,#4a4a4a 40%,#2a2a2a 100%)}
.attorney{position:absolute;top:560px;font-size:13px;font-style:italic;color:#333}

/* value */
.section-title{position:absolute;left:0;width:1200px;text-align:center;font-size:29px;color:var(--ink);font-weight:400}
.section-title b{font-weight:900}
.value-item{position:absolute;top:683px;width:300px;text-align:center}
.ring{margin:0 auto;display:block}
.value-item h3{margin-top:18px;font-size:21px;line-height:28px;font-weight:900;color:var(--orange);text-transform:uppercase}
.value-item p{margin-top:4px;font-size:17px;line-height:27.5px;color:var(--ink)}

/* bottom line */
.bottom-line{position:absolute;left:0;top:1053px;width:1200px;height:418px;background:var(--blue)}
.bottom-line h2{position:absolute;left:0;width:1200px;top:40px;text-align:center;font-size:29px;color:var(--white);font-weight:400}
.bottom-line h2 b{font-weight:900}
.bottom-line p{position:absolute;left:132px;width:936px;top:96px;text-align:center;font-size:20.5px;line-height:27px;color:var(--white)}
.bottom-line .promise{position:absolute;left:0;width:1200px;top:228px;text-align:center;font-size:31px;font-weight:900;color:var(--white)}
.cta{position:absolute;left:433px;top:296px;width:347px;height:67px;background:var(--orange);color:var(--ink);text-align:center;box-shadow:6px 6px 0 rgba(0,0,0,.35)}
.cta .t{display:block;padding-top:7px;font-size:22px;font-weight:900;letter-spacing:1.5px}
.cta .n{display:block;font-size:21px;color:var(--white);font-weight:700}

/* process */
.process{position:absolute;left:0;top:1471px;width:1200px;height:415px;background:var(--grey-bg)}
.step{position:absolute;top:101px;width:300px;text-align:center}
.step h3{margin-top:22px;font-size:17px;line-height:22px;color:var(--orange);font-weight:900;text-transform:uppercase}
.step h3 span{display:block;font-weight:400}
.step p{margin-top:10px;font-size:16.5px;line-height:27px;color:var(--ink)}

/* contact */
.scene{position:absolute;left:0;top:1886px;width:1200px;height:836px;
  background:linear-gradient(180deg,#4a8fc4 0%,#8bbde0 35%,#cfd9dc 58%,#b9a78c 70%,#7b8a92 80%,#5d7e93 100%)}
.ask-box{position:absolute;left:373px;top:2000px;width:464px;height:628px;background:rgba(133,202,230,.55);border-radius:6px}
.ask-box .q{position:absolute;left:0;width:464px;top:30px;text-align:center;font-size:31px;letter-spacing:5px;color:var(--white);font-weight:700}
.field{position:absolute;left:25px;width:412px;background:var(--white);font-size:14px;color:#aaa;padding:18px 14px 0}
.ask-box .a{position:absolute;left:0;width:464px;top:488px;text-align:center;font-size:31px;letter-spacing:5px;color:var(--white);font-weight:700}
.ask-btn{position:absolute;left:25px;top:535px;width:412px;height:63px;background:var(--orange);color:var(--white);text-align:center;line-height:63px;font-size:22px;font-weight:900;letter-spacing:4px}

/* footer */
.addr{position:absolute;left:67px;top:2766px;font-size:14px;line-height:21px;color:var(--blue-deep)}
.foot-logo{position:absolute;left:0;width:1200px;top:2802px;text-align:center;font-size:28px;font-weight:700;color:var(--blue)}
.bar-note{position:absolute;left:893px;top:2766px;width:280px;font-size:14px;line-height:21px;color:var(--blue-deep)}
.legal{position:absolute;left:0;top:2906px;width:1200px;height:35px;background:var(--dark-bar);color:var(--white);font-size:13px;text-align:center;line-height:35px}
</style>
</head>
<body>

<section class="hero">
  <div class="hero-frame"></div>
  <div class="portrait left" role="img" aria-label="Portrait photo of attorney in dark suit and striped tie"></div>
  <div class="portrait right" role="img" aria-label="Portrait photo of attorney in grey suit"></div>
  <div class="hero-kicker"><span>YOUR INJURY CASE IS IMPORTANT</span></div>
  <h1 class="hero-title"><b>KNOW</b> YOUR LAWYER</h1>
  <p class="hero-copy">With Hollowmere Law Group, you will talk to your lawyer on your first call. No screener, no receptionist, just instant advice. You will know your lawyer.</p>
  <div class="hero-btn">504-617-2093</div>
  <div class="attorney" style="left:415px">Owen R. Hollowmere, Esq</div>
  <div class="attorney" style="left:670px">Miles D. Carrow, Esq</div>
  <div class="logo">HOLLOWMERE LAW GROUP</div>
  <nav class="nav">
    <span class="active">Home</span><span>Our Value</span><span>Bottom Line</span><span>Our Process</span><span>Quick Question</span>
  </nav>
</section>

<h2 class="section-title" style="top:620px"><b>OUR VALUE</b> TO YOU</h2>

<div class="value-item" style="left:117px">
  <svg class="ring" width="152" height="152" viewBox="0 0 152 152">
    <circle cx="76" cy="76" r="73" fill="#fff" stroke="#33a6d7" stroke-width="3"/>
    <polygon points="76,22 123,49 123,103 76,130 29,103 29,49" fill="#f78f20"/>
    <circle cx="76" cy="76" r="22" fill="none" stroke="#fff" stroke-width="4"/>
    <text x="76" y="86" text-anchor="middle" font-family="Lato,sans-serif" font-weight="900" font-size="28" fill="#fff">$</text>
  </svg>
  <h3>Your Case, Your<br>Money</h3>
  <p>Our law firm is structured to make sure that we charge less so you can keep more. Call and ask us about how we do it.</p>
</div>
<div class="value-item" style="left:450px">
  <svg class="ring" width="152" height="152" viewBox="0 0 152 152">
    <circle cx="76" cy="76" r="73" fill="#fff" stroke="#33a6d7" stroke-width="3"/>
    <polygon points="76,22 123,49 123,103 76,130 29,103 29,49" fill="#f78f20"/>
    <rect x="54" y="62" width="44" height="32" rx="4" fill="#fff"/>
    <rect x="66" y="54" width="20" height="10" rx="2" fill="none" stroke="#fff" stroke-width="4"/>
  </svg>
  <h3>History of<br>Success</h3>
  <p>Through trial or settlement, we have successfully recovered hundreds of thousands of dollars for our clients.</p>
</div>
<div class="value-item" style="left:780px">
  <svg class="ring" width="152" height="152" viewBox="0 0 152 152">
    <circle cx="76" cy="76" r="73" fill="#fff" stroke="#33a6d7" stroke-width="3"/>
    <polygon points="76,22 123,49 123,103 76,130 29,103 29,49" fill="#f78f20"/>
    <rect x="64" y="58" width="26" height="38" rx="13" fill="none" stroke="#fff" stroke-width="3" transform="rotate(-40 77 77)"/>
    <path d="M60 62 Q56 54 62 50" fill="none" stroke="#fff" stroke-width="3"/>
  </svg>
  <h3>We Make This<br>Easy</h3>
  <p>Our law firm uses the most cutting edge technology to work on your terms, your schedule, and always be accessible.</p>
</div>

<section class="bottom-line">
  <h2><b>THE BOTTOM</b> LINE</h2>
  <p>Our mission: to do great work for our clients and not overcharge them for it. TV lawyers charge big fees so they can run commercials. The bigger the billboard, the bigger the client’s bill. By using only the most cutting edge digital technology, our firm creates savings that we pass directly to our clients. The bottom line:</p>
  <div class="promise">WITH US YOU'LL KEEP MORE OF YOUR MONEY</div>
  <div class="cta"><span class="t">GET HELP NOW</span><span class="n">504-617-2093</span></div>
</section>

<section class="process">
  <h2 class="section-title" style="top:40px"><b>OUR PROCESS WORKS</b> FOR YOU</h2>
  <div class="step" style="left:62px">
    <svg class="ring" width="112" height="112" viewBox="0 0 112 112">
      <circle cx="56" cy="56" r="52" fill="#fff" stroke="#33a6d7" stroke-width="8"/>
      <polygon points="56,18 89,37 89,75 56,94 23,75 23,37" fill="#fff" stroke="#33a6d7" stroke-width="2"/>
      <path d="M42 64 a14 12 0 1 1 8 6 l-8 4 z" fill="none" stroke="#f78f20" stroke-width="3"/>
      <circle cx="64" cy="62" r="8" fill="#f78f20"/>
    </svg>
    <h3>Free<span>Consultation</span></h3>
    <p>It’s always free to reach out to us and talk. Let’s see how we can help.</p>
  </div>
  <div class="step" style="left:438px">
    <svg class="ring" width="112" height="112" viewBox="0 0 112 112">
      <circle cx="56" cy="56" r="52" fill="#fff" stroke="#33a6d7" stroke-width="8"/>
      <polygon points="56,18 89,37 89,75 56,94 23,75 23,37" fill="#fff" stroke="#33a6d7" stroke-width="2"/>
      <circle cx="56" cy="56" r="17" fill="none" stroke="#f78f20" stroke-width="4"/>
      <text x="56" y="64" text-anchor="middle" font-family="Lato,sans-serif" font-weight="900" font-size="22" fill="#f78f20">$</text>
      <line x1="44" y1="44" x2="68" y2="68" stroke="#f78f20" stroke-width="4"/>
    </svg>
    <h3>No Fee<span>Unless We Win</span></h3>
    <p>The way we structure our fees, we never get paid unless you do too.</p>
  </div>
  <div class="step" style="left:827px">
    <svg class="ring" width="112" height="112" viewBox="0 0 112 112">
      <circle cx="56" cy="56" r="52" fill="#fff" stroke="#33a6d7" stroke-width="8"/>
      <polygon points="56,18 89,37 89,75 56,94 23,75 23,37" fill="#fff" stroke="#33a6d7" stroke-width="2"/>
      <circle cx="56" cy="56" r="19" fill="#f78f20"/>
      <circle cx="56" cy="51" r="6" fill="#fff"/>
      <path d="M45 68 q11 -14 22 0" fill="#fff"/>
    </svg>
    <h3>Personal<span>Representation</span></h3>
    <p>Unlike the lawyer on the billboard, you’ll know us personally.</p>
  </div>
</section>

<div class="scene" role="img" aria-label="Photo of the New Orleans skyline across the river under a blue sky"></div>
<form class="ask-box">
  <div class="q">QUICK QUESTION?</div>
  <div class="field" style="top:79px;height:53px">Name</div>
  <div class="field" style="top:151px;height:53px">Phone</div>
  <div class="field" style="top:224px;height:53px">E-mail</div>
  <div class="field" style="top:298px;height:163px">Subject</div>
  <div class="a">QUICK ANSWER</div>
  <div class="ask-btn">ASK</div>
</form>

<svg class="abs" style="left:34px;top:2766px" width="22" height="26" viewBox="0 0 22 26">
  <path d="M11 1 C5 1 1 5 1 10 C1 17 11 25 11 25 C11 25 21 17 21 10 C21 5 17 1 11 1 Z" fill="#33a6d7"/>
  <circle cx="11" cy="10" r="4" fill="#fff"/>
</svg>
<div class="addr">48 Harbor Lane New Orleans, La<br>70000 504-617-2093</div>
<div class="foot-logo">HOLLOWMERE LAW GROUP</div>
<div class="bar-note">Barred in all Louisiana State courts, and the Eastern, Middle and Western federal district courts of Louisiana.</div>
<div class="legal">All rights reserved 2016 &nbsp;Hollowmere Law Group</div>

</body>
</html>
```